Specialty Chemical Product Line Card Revamp

I need a new digital brochure for our product catalog of various chemicals. This will be sent to my customers as a digital file or printed on flat paper (not a folded brochure). I have included the OLD brochure (Tobin Chemical Line Card document) and the new categories that I want used instead (Line Card Categories document). I also included our logo and other photos. I would like the new brochure to be more modern and attention-grabbing

Target Market(s)

Product Manufacturers

Industry/Entity Type

Chemical Product

Font styles to use
Serif
Sans Serif

Requirements
Must have
• Product Category Headers. Company Logo
Nice to have
• Incorporate the attached photos. Use similar colors as the logo. Fit on 2 pages
Should not have
• Cannot be more than 3 pages.

```html
<!DOCTYPE html>
<html lang="en">
<head>
<meta charset="utf-8">
<title>Tobin Chemical Line Card</title>
<link href="https://fonts.googleapis.com/css2?family=Heebo:wght@400&family=Noto+Serif:wght@700&display=swap" rel="stylesheet">
<style>
:root{
  --stage:#6a58a6;
  --paper:#f0f0f1;
  --green:#88b86a;
  --purple:#4b3b78;
  --ink:#4a4a4f;
  --ink-dark:#333338;
  --white:#ffffff;
}
*{margin:0;padding:0;box-sizing:border-box}
html,body{width:1135px;height:1200px;overflow:hidden;background:var(--stage)}
.line-card{position:absolute;left:161px;top:20px;width:813px;height:1160px;background:var(--paper);font-family:"Heebo",sans-serif;color:var(--ink);font-size:11.2px}
.band{position:absolute;left:28px;width:757px;height:36px;display:flex;align-items:center;justify-content:center;color:var(--white);font-family:"Noto Serif",serif;font-weight:700;font-size:23px;letter-spacing:3px}
.band--green{background:var(--green)}
.band--purple{background:var(--purple)}
.function-panel{position:absolute;left:0;top:824px;width:813px;height:273px;background:var(--purple)}
.items{position:absolute;list-style:none;line-height:16.6px;white-space:nowrap}
.items li{position:relative;padding-left:13px}
.items li::before{content:"";position:absolute;left:1px;top:5.5px;width:4px;height:4px;border-radius:50%;background:var(--green)}
.items li.cont::before{display:none}
.items--light{color:var(--white)}
.items--light li::before{background:var(--white)}
.footer-contact{position:absolute;left:0;top:1107px;width:813px;text-align:center;font-family:"Noto Serif",serif;font-weight:700;font-size:23px;letter-spacing:2.4px;color:var(--ink-dark)}
.footer-bar{position:absolute;left:0;bottom:0;width:813px;height:13px;background:var(--green)}
</style>
</head>
<body>
<main class="line-card">

  <h2 class="band band--green" style="top:42px">SODIUM COMPOUNDS</h2>
  <ul class="items" style="left:31px;top:93px">
    <li>Disodium Phosphate, FCC</li><li>Monosodium Phosphate</li><li>Sodium Acetate</li><li>Sodium Benzoate</li><li>Sodium Bichromate</li><li>Sodium Bisulfate, Anhy G.B.S.</li><li>Sodium Bisulfite, liquid</li><li>Sodium Bicarbonite</li><li>Sodium Bifluoride</li><li>Sodium Canide</li>
  </ul>
  <ul class="items" style="left:214px;top:93px">
    <li>Sodium Chlorate</li><li>Sodium Citrate, USP granular</li><li>Sodium Fluoride</li><li>Sodium Gluconate</li><li>Sodium Hexametaphosphate, Tech</li><li>Sodium Hexametaphosphate, Food grade</li><li>Sodium Hydrosulfite</li><li>Sodium Hypochlorite</li><li>Sodium Metasilicate, Anhy. Drysil</li><li>Sodium Metasilicate, Pent. Crystasil</li>
  </ul>
  <ul class="items" style="left:448px;top:93px">
    <li>Sodium Molybdate</li><li>Sodium Nitrate</li><li>Sodium Nitrite</li><li>Sodium Percarbonate</li><li>Sodium Permanganate</li><li>Sodium Persulfate</li><li>Sodium Acid Pyrophosphate</li><li>Sodium Silicate</li><li>Sodium Silicofluoride</li><li>Sodium Sulfide</li>
  </ul>
  <ul class="items" style="left:617px;top:93px">
    <li>Sodium Sulfate</li><li>Sodium Sulfate, Anhydrous</li><li>Sodium Thiosulate, liquid or dry</li><li>Sodium Tripolyphosphate, Anhy.</li><li>Gran. Lite</li><li>Sodium Tripolyphosphate, Anhy.</li><li>Gran. Tech</li><li>Tetra Sodium Pyro Phosphate,</li><li>FCC</li><li>Trisodium Phosphate</li>
  </ul>

  <h2 class="band band--purple" style="top:287px">AMINES</h2>
  <ul class="items" style="left:31px;top:337px">
    <li>Cyclohexylamine</li><li>DEA 99%</li><li>Diethylamine</li>
  </ul>
  <ul class="items" style="left:214px;top:338px">
    <li>Diethylethanolamine</li><li>Dimethyl Ethanolamine</li><li>Ethylenediamine</li>
  </ul>
  <ul class="items" style="left:429px;top:337px">
    <li>Monoethanolamine</li><li>Morpholine</li>
  </ul>
  <ul class="items" style="left:618px;top:337px">
    <li>Triethylolamine 85%, 99%</li><li>Triethylamine</li>
  </ul>

  <h2 class="band band--green" style="top:410px">SOLIDS</h2>
  <ul class="items" style="left:31px;top:457px">
    <li>Activated Carbon</li><li>Anhydrous Ammonia</li><li>Aluminum Sulfate</li><li>Barium Carbonate</li><li>Bicarbonate of Soda</li><li>CCH Granular 65% (PCG)</li><li>Calcium Boride</li><li>Calcium Chloride, flake or</li><li class="cont">pellets</li><li>Calcium Nitrate</li>
  </ul>
  <ul class="items" style="left:214px;top:457px">
    <li>Caustic Potash, flake</li><li>Caustic Soda, beads or flake</li><li>Citric Acid, USP</li><li>Copper Cyanide</li><li>Copper Sulfate, crystal</li><li>Dipotassium Phosphate, FCC</li><li>Disodium Phosphate, FCC</li><li>Epsom Salts</li><li>Manganese Sulfate, dry</li><li>Muriate of Potash</li>
  </ul>
  <ul class="items" style="left:429px;top:457px">
    <li>Nickel Chloride, dry</li><li>Nickel Sulfate, salt</li><li>Oil Sorb Adsorbent</li><li>Pelacal</li><li>Rochelle Salts</li><li>Rock Salt</li><li>Sodium Bisulfate, Anhy G.B.S.</li><li>Sodium Citrate, USP granular</li><li>Sodium Metasilicate, Anhy. Drysil</li><li>Sodium Sulfate, Anhydrous</li>
  </ul>
  <ul class="items" style="left:622px;top:457px">
    <li>Sodium Thiosulate, dry</li><li>Sodium Tripolyphosphate,</li><li class="cont">Anhy. Gran. Lite</li><li>Sodium Tripolyphosphate,</li><li class="cont">Anhy. Gran. Tech</li><li>Tetra Potassium Pyro</li><li>Phosphate, Gran. Tech</li><li>Zinc Dust</li>
  </ul>

  <h2 class="band band--purple" style="top:647px">MISCELLANEOUS</h2>
  <ul class="items" style="left:31px;top:696px">
    <li>All Purpose Cleaner</li><li>Bleach</li><li>Polywax</li><li>Caustic Soda Liquid 50%,</li><li>Diaphragm Grade</li>
  </ul>
  <ul class="items" style="left:214px;top:696px">
    <li>Caustic Soda Liquid,</li><li>Membrane Grade</li><li>Distilled Water</li><li>Glyfrost</li><li>Thermflo</li>
  </ul>
  <ul class="items" style="left:429px;top:697px">
    <li>Formaldehyde 37%</li><li>Hydrogen Peroxide, Tech,</li><li>Food Grade</li><li>Potsil (Potassium Silicate)</li><li>Quik Sorb</li>
  </ul>
  <ul class="items" style="left:626px;top:697px">
    <li>Soaps</li><li>Polyols</li><li>Urea</li><li>Winshield Washer Solvent</li>
  </ul>

  <section class="function-panel"></section>
  <h2 class="band band--green" style="top:807px">BY FUNCTION</h2>
  <ul class="items items--light" style="left:31px;top:858px">
    <li>Antifoams</li><li>Antifreeze</li><li>Blanket/Roller Wash</li><li>Chelating Agents</li><li>Chlorinated Solvents</li><li>Cleaners, Floor, Metal,</li><li>Soak, Steam</li><li>Coolants</li><li>Corrosion Inhibitors</li><li>Cutting Oils</li><li>Dechlorinators</li><li>Defoamers</li><li>Degreasing Solvents</li>
  </ul>
  <ul class="items items--light" style="left:214px;top:858px">
    <li>De-Icers</li><li>Descaling Acid</li><li>Electro Cleaners</li><li>Filter Powders</li><li>Floor Adsorbents</li><li>Foam Control</li><li>Form Oils</li><li>Gear Oils</li><li>Heat Transfer Fluids</li><li>Hydraulic Fluids</li><li>Inhibited Glycol Fluids</li><li>Lacquer Reducers</li><li>Lacquer Thinners</li>
  </ul>
  <ul class="items items--light" style="left:429px;top:858px">
    <li>Laboratory Chemicals</li><li>Metal Cleaners</li><li>Metal Conditioners</li><li>Metalworking Lubricants</li><li>Nonionic Surfactants</li><li>Paint Strippers</li><li>Paint Thinners</li><li>Process Oils</li><li>Reagent Acids</li><li>Reagent Solvents</li><li>Rubber Rejuvenator</li><li>Rust Proofers</li><li>Safety Absorbent</li>
  </ul>
  <ul class="items items--light" style="left:632px;top:858px">
    <li>Safety Solvents</li><li>Soak Cleaners</li><li>Soluble Oils</li><li>Steam Cleaners</li><li>Surfactants</li><li>Synthetic Coolants</li><li>Thinners</li><li>Waste Water Treatment</li><li>Solutions</li><li>Water Soluble Oils</li><li>Wetting Agents</li>
  </ul>

  <p class="footer-contact">12 555 01470 | WWW.TOBINCHEMICAL.COM</p>
  <div class="footer-bar"></div>
</main>
</body>
</html>
```